Chicago Train Advertisement for HomeAlongRail.com.

We have purchased one month of advertising on the Chicago NRX subway train. We will have 150 cards up in the subway to advertise our website HomeAlongRail.com where people can search for properties by train station. The cards are 11" tall and 46.5" long. We want people to feel compelled to jump on their cell phones and conduct a search for an apartment or home while they are riding the train, or at least enter their email and search criteria so one of our agents can help them.

Target Market(s)

People who want to live near train stations

Industry/Entity Type

Real Estate

Font styles to use
Sans Serif

Colors

Designer to choose colors to be used in the design.

Requirements
Must have
• The homealongrail logo and a catchy slogan, something like: Find your home near a train station the easy way: www.homealongral.com. Search real estate listings near the NRX or Velco.

```html
<!DOCTYPE html>
<html lang="en">
<head>
<meta charset="utf-8">
<title>HomeAlongRail.com – Train Cards</title>
<link href="https://fonts.googleapis.com/css2?family=Arimo:wght@400;700&display=swap" rel="stylesheet">
<style>
  :root {
    --page-bg: #ffffff;
    --card-bg: #f7f7f7;
    --card-border: #c9c9c9;
    --headline-blue: #2b9ad6;
    --arc-light: #6cbde8;
    --arc-dark: #1a97d8;
    --body-text: #333333;
    --brand-navy: #2a3a6b;
  }
  * { margin: 0; padding: 0; box-sizing: border-box; }
  html, body {
    width: 1200px;
    height: 602px;
    overflow: hidden;
    background: var(--page-bg);
    font-family: "Arimo", Arial, sans-serif;
  }
  .canvas {
    position: relative;
    width: 1200px;
    height: 602px;
  }
  .train-card {
    position: absolute;
    left: 0;
    width: 1200px;
    height: 286px;
    background: var(--card-bg);
    border: 1px solid var(--card-border);
    overflow: hidden;
  }
  .train-card--top { top: 0; }
  .train-card--bottom { top: 316px; }
  .card-visual {
    position: absolute;
    left: 0;
    top: 0;
    width: 620px;
    height: 286px;
  }
  .headline {
    position: absolute;
    left: 603px;
    top: 66px;
    color: var(--headline-blue);
    font-weight: 700;
    font-size: 30px;
    line-height: 39px;
    letter-spacing: -0.2px;
  }
  .info-block {
    position: absolute;
    right: 43px;
    top: 96px;
    width: 300px;
    text-align: center;
  }
  .tagline {
    color: var(--body-text);
    font-size: 21px;
    line-height: 28px;
  }
  .brand-name {
    display: flex;
    align-items: center;
    justify-content: flex-end;
    gap: 8px;
    margin-top: 36px;
    padding-right: 6px;
    color: var(--brand-navy);
    font-size: 20px;
    font-weight: 400;
  }
  .brand-dot {
    width: 14px;
    height: 14px;
    border-radius: 50%;
    background: var(--brand-navy);
  }
  .web-address {
    margin-top: 10px;
    text-align: right;
    color: #111111;
    font-size: 22px;
  }
</style>
</head>
<body>
<main class="canvas">

  <section class="train-card train-card--top">
    <svg class="card-visual" viewBox="0 0 620 286" aria-hidden="false">
      <defs>
        <linearGradient id="housesTone" x1="0" y1="0" x2="1" y2="1">
          <stop offset="0" stop-color="#dfe3e8"/>
          <stop offset="0.5" stop-color="#c9ced6"/>
          <stop offset="1" stop-color="#aab2bc"/>
        </linearGradient>
      </defs>
      <path d="M0 0 H551 C615 80 605 220 436 286 H0 Z" fill="var(--arc-dark)"/>
      <path d="M0 0 H482 C562 70 562 210 418 286 H0 Z" fill="var(--arc-light)"/>
      <path role="img" aria-label="Photo: a hand holding small white model houses floating in the air"
            d="M0 0 H458 C530 60 538 200 393 286 H0 Z" fill="url(#housesTone)"/>
    </svg>
    <h2 class="headline">Search For<br>Properties That<br>Fit Your Lifestyle.</h2>
    <div class="info-block">
      <p class="tagline">Search real estate listings<br>near the NRX or Velco.</p>
      <p class="brand-name"><span class="brand-dot"></span>HomeAlongRail.com</p>
      <p class="web-address">www.homealongral.com.</p>
    </div>
  </section>

  <section class="train-card train-card--bottom">
    <svg class="card-visual" viewBox="0 0 620 286" aria-hidden="false">
      <defs>
        <linearGradient id="skylineTone" x1="0" y1="0" x2="0" y2="1">
          <stop offset="0" stop-color="#5f7f9e"/>
          <stop offset="0.35" stop-color="#a9bccd"/>
          <stop offset="0.6" stop-color="#6f7a7e"/>
          <stop offset="0.78" stop-color="#4f6e63"/>
          <stop offset="1" stop-color="#3f6f86"/>
        </linearGradient>
      </defs>
      <path d="M0 0 H551 C615 80 605 220 436 286 H0 Z" fill="var(--arc-dark)"/>
      <path d="M0 0 H482 C562 70 562 210 418 286 H0 Z" fill="var(--arc-light)"/>
      <path role="img" aria-label="Photo: city skyline with skyscrapers beside a lakefront shoreline under a cloudy sky"
            d="M0 0 H458 C530 60 538 200 393 286 H0 Z" fill="url(#skylineTone)"/>
    </svg>
    <h2 class="headline">Search For<br>Properties That<br>Fit Your Lifestyle.</h2>
    <div class="info-block">
      <p class="tagline">Search real estate listings<br>near the NRX or Velco.</p>
      <p class="brand-name"><span class="brand-dot"></span>HomeAlongRail.com</p>
      <p class="web-address">www.homealongral.com.</p>
    </div>
  </section>

</main>
</body>
</html>
```